Zielgruppe
We are an event technology rental company specializing in corporate events and conferences. Our services include audio and video rental, LED video walls, and full technical support for business events of all sizes
Aufgabenstellung
Objective:
To design and develop a modern, visually appealing website that effectively communicates our brand values: experience, trustworthiness, and professionalism. The site should support our sales and marketing efforts by showcasing our services, building credibility, and making it easy for potential clients to get in touch.
Creative Direction:
• The website should feature eye-catching visuals
• It should have a clean, professional design with a user-friendly interface and intuitive navigation.
• The look and feel must reflect technical competence, reliability, and high-end service.
Content & Structure Guidelines:
A basic guide with suggested sections is provided in the attachment.
⚠️ Please note:
• The guide is not a layout or color reference.
• It serves only to suggest the types of content sections we want.
• The order of sections is flexible — we welcome your creative interpretation.
Header Feature:
The website header should be designed to support a 10–12 second video in the future. For now, please use a stock photo (not one of our own images) as a placeholder.
Visual & UX Expectations:
• Strong visual hierarchy and clarity.
• Mobile-optimized, responsive design.
• Fast-loading and modern layout.
• Clear calls to action such as “Contact” or “Request a Quote”
• A smooth, professional user experience with a focus on technical services.

```html
<!DOCTYPE html>
<html lang="de">
<head>
<meta charset="utf-8">
<title>Klangraum Technik – Startseite</title>
<link rel="stylesheet" href="https://fonts.googleapis.com/css2?family=Inter:wght@400;500;600;700;800&display=swap">
<style>
  :root {
    --green: #19a35f;
    --green-dark: #138a4f;
    --ink: #121a1b;
    --white: #ffffff;
    --hero-deep: #13302f;
    --band: #0b2324;
    --rule: #e4e7e7;
    --sky-warm: #d98a6a;
    --sky-cool: #6e8c93;
  }
  * { box-sizing: border-box; margin: 0; padding: 0; }
  html, body { width: 1200px; height: 1200px; overflow: hidden; }
  body {
    font-family: "Inter", sans-serif;
    background: var(--white);
    color: var(--ink);
  }
  .page { width: 1200px; height: 1200px; display: flex; flex-direction: column; }

  /* Header */
  .site-header {
    height: 150px;
    display: flex;
    align-items: center;
    justify-content: space-between;
    padding: 0 60px 0 90px;
    background: var(--white);
  }
  .brand { display: flex; align-items: center; gap: 16px; }
  .brand-dot { width: 40px; height: 40px; border-radius: 50%; background: var(--green); }
  .brand-name { font-size: 22px; font-weight: 600; line-height: 1.15; color: var(--ink); width: 230px; }
  .header-right { display: flex; flex-direction: column; align-items: flex-end; gap: 22px; }
  .contact-row { display: flex; gap: 12px; }
  .contact-chip {
    display: flex; align-items: center; gap: 8px;
    height: 36px; padding: 0 16px; border-radius: 4px;
    font-size: 14px; font-weight: 600; white-space: nowrap;
  }
  .contact-chip--phone { border: 1.5px solid var(--ink); color: var(--ink); }
  .contact-chip--mail { background: var(--green); color: var(--white); }
  .main-nav {
    display: flex; gap: 30px;
    font-size: 15px; font-weight: 600;
    border-top: 1px solid var(--rule); padding-top: 12px;
  }
  .main-nav a { color: var(--ink); text-decoration: none; white-space: nowrap; }
  .main-nav a.is-active { color: var(--green); }

  /* Hero */
  .hero { position: relative; flex: 1; overflow: hidden; }
  .hero-media {
    position: absolute; inset: 0;
    background:
      linear-gradient(90deg, rgba(19,48,47,.96) 0%, rgba(19,48,47,.78) 40%, rgba(19,48,47,0) 75%),
      linear-gradient(180deg, var(--sky-cool) 0%, var(--sky-warm) 38%, #3a4448 52%, #1d2a2d 75%, #141e20 100%);
  }
  .hero-content {
    position: relative; z-index: 1;
    padding: 200px 0 0 100px; width: 760px; color: var(--white);
  }
  .hero-title { font-size: 60px; font-weight: 700; line-height: 1.12; letter-spacing: -0.5px; }
  .hero-lead { margin-top: 28px; font-size: 17px; line-height: 1.6; width: 560px; opacity: .95; }
  .hero-actions { margin-top: 36px; display: flex; gap: 14px; }
  .btn {
    height: 46px; padding: 0 24px; display: inline-flex; align-items: center;
    font-size: 15px; font-weight: 600; border-radius: 2px; color: var(--white);
    white-space: nowrap; flex-shrink: 0;
  }
  .btn--primary { background: var(--green); }
  .btn--secondary { border: 2px solid var(--white); }

  /* Service band */
  .service-band {
    height: 200px; background: var(--band);
    display: flex; align-items: center; justify-content: space-between;
    gap: 40px;
    padding: 0 70px 0 100px; color: var(--white);
  }
  .service-list { display: flex; gap: 34px; list-style: none; }
  .service-item { display: flex; align-items: center; gap: 12px; font-size: 28px; font-weight: 700; white-space: nowrap; }
  .tick { width: 28px; height: 28px; flex-shrink: 0; }
  .btn--outline-small {
    border: 2px solid var(--white); height: 42px; padding: 0 18px;
    font-size: 14px; font-weight: 600; gap: 10px;
  }
</style>
</head>
<body>
<div class="page">
  <header class="site-header">
    <div class="brand">
      <span class="brand-dot"></span>
      <span class="brand-name">Klangraum Technik Produktions GmbH</span>
    </div>
    <div class="header-right">
      <div class="contact-row">
        <span class="contact-chip contact-chip--phone">
          <svg width="16" height="16" viewBox="0 0 24 24" fill="none" stroke="#19a35f" stroke-width="2.2" stroke-linecap="round" stroke-linejoin="round"><path d="M22 16.9v3a2 2 0 0 1-2.2 2 19.8 19.8 0 0 1-8.6-3.1 19.5 19.5 0 0 1-6-6A19.8 19.8 0 0 1 2.1 4.2 2 2 0 0 1 4.1 2h3a2 2 0 0 1 2 1.7c.1 1 .4 1.900.7 2.8a2 2 0 0 1-.5 2.1L8 9.9a16 16 0 0 0 6 6l1.3-1.3a2 2 0 0 1 2.1-.4c.9.3 1.800.6 2.800.7a2 2 0 0 1 1.700 2z"/></svg>
          +43 1 555 0187
        </span>
        <span class="contact-chip contact-chip--mail">
          <svg width="16" height="16" viewBox="0 0 24 24" fill="none" stroke="#ffffff" stroke-width="2" stroke-linejoin="round"><rect x="3" y="5" width="18" height="14" rx="1"/><path d="M3 6l9 7 9-7"/></svg>
          office@klangraum-technik.at
        </span>
      </div>
      <nav class="main-nav">
        <a href="#" class="is-active">Start</a>
        <a href="#">Ihr Event</a>
        <a href="#">News &amp; Angebote</a>
        <a href="#">Unsere Technik</a>
        <a href="#">Crew</a>
        <a href="#">Kontakt</a>
      </nav>
    </div>
  </header>

  <section class="hero">
    <div class="hero-media" role="img" aria-label="Abendliche Stadtansicht über Dächern mit Kirchturm und Hügeln im Sonnenuntergang"></div>
    <div class="hero-content">
      <h1 class="hero-title">Eventtechnik trifft digitale Inszenierung.</h1>
      <p class="hero-lead">Lorem ipsum dolor sit amet, consetetur sadipscing elitr, sed diam nonumy eirmod tempor invidunt ut labore et dolore magna aliquyam erat, sed diam voluptua. At vero eos et accusam et.</p>
      <div class="hero-actions">
        <span class="btn btn--primary">Button-Primary</span>
        <span class="btn btn--secondary">Button-Secondary</span>
      </div>
    </div>
  </section>

  <section class="service-band">
    <ul class="service-list">
      <li class="service-item"><svg class="tick" viewBox="0 0 30 30"><rect width="30" height="30" rx="4" fill="#19a35f"/><path d="M8 15l5 5 9-11" fill="none" stroke="#fff" stroke-width="3" stroke-linecap="round" stroke-linejoin="round"/></svg>Ton</li>
      <li class="service-item"><svg class="tick" viewBox="0 0 30 30"><rect width="30" height="30" rx="4" fill="#19a35f"/><path d="M8 15l5 5 9-11" fill="none" stroke="#fff" stroke-width="3" stroke-linecap="round" stroke-linejoin="round"/></svg>Licht</li>
      <li class="service-item"><svg class="tick" viewBox="0 0 30 30"><rect width="30" height="30" rx="4" fill="#19a35f"/><path d="M8 15l5 5 9-11" fill="none" stroke="#fff" stroke-width="3" stroke-linecap="round" stroke-linejoin="round"/></svg>Video</li>
      <li class="service-item"><svg class="tick" viewBox="0 0 30 30"><rect width="30" height="30" rx="4" fill="#19a35f"/><path d="M8 15l5 5 9-11" fill="none" stroke="#fff" stroke-width="3" stroke-linecap="round" stroke-linejoin="round"/></svg>Streaming</li>
      <li class="service-item"><svg class="tick" viewBox="0 0 30 30"><rect width="30" height="30" rx="4" fill="#19a35f"/><path d="M8 15l5 5 9-11" fill="none" stroke="#fff" stroke-width="3" stroke-linecap="round" stroke-linejoin="round"/></svg>LED</li>
    </ul>
    <span class="btn btn--outline-small">Jetzt alle Leistungen ansehen!
      <svg width="12" height="16" viewBox="0 0 12 16" fill="none" stroke="#19a35f" stroke-width="2" stroke-linecap="round" stroke-linejoin="round"><path d="M6 1v13M1 9l5 5 5-5"/></svg>
    </span>
  </section>
</div>
</body>
</html>
```